Cover Art Needed For Digital Single Release

We are looking to have the cover art designed for a new song called "Paper Lanterns". You will find the track attached below in a private TuneVault link so that you can have a listen.
We are thinking of keeping the artwork fairly simple but still want it to catch your eye. Maybe using the song title and artist’s name in a colorful and creative way. (A well-designed font with a bold color scheme, or even something like a mosaic style art piece featuring the title).
We completely welcome any and all creative visions you might have, even if it strays away from the examples given above.
Thank you in advance for your submissions, and we are excited to collaborate with you!
"Paper Lanterns" by Marcus Holloway
https://tunevault.example/marcusxyz/paper-lanterns/s-r7Tq2wLmNcx
Target Market(s)
Teens/Young Adults
Industry/Entity Type
Music
Requirements
Must have
- An eye-catching design
Should not have
- Please do not rely heavily on stock images. We prefer an original design/concept.

```html
<!DOCTYPE html>
<html lang="en">
<head>
<meta charset="utf-8">
<title>Paper Lanterns – Marcus Holloway</title>
<link rel="stylesheet" href="https://fonts.googleapis.com/css2?family=Anton&display=swap">
<style>
  :root {
    --paper: #e8e8e8;
    --paper-light: #f5f5f5;
    --ink: #000000;
    --mosaic-red: #e8000b;
    --mosaic-orange: #fb5a0a;
    --mosaic-yellow: #f4cd38;
    --mosaic-gold: #f0a80c;
  }
  html, body {
    margin: 0;
    padding: 0;
    overflow: hidden;
  }
  .cover {
    position: relative;
    width: 1200px;
    height: 1200px;
    overflow: hidden;
    background: var(--paper);
    font-family: "Anton", "Impact", sans-serif;
  }
  .title-band {
    position: absolute;
    left: 0;
    top: 0;
    width: 1200px;
    height: 502px;
    overflow: hidden;
    background: var(--paper);
  }
  .backdrop-letters {
    position: absolute;
    left: -180px;
    top: -160px;
    font-size: 760px;
    line-height: 1;
    color: var(--paper-light);
    white-space: nowrap;
    user-select: none;
  }
  .title-block {
    position: absolute;
    right: 135px;
    top: 22px;
    margin: 0;
    display: flex;
    flex-direction: column;
    align-items: flex-start;
    color: var(--ink);
    font-weight: 400;
  }
  .title-line {
    display: block;
    font-size: 160px;
    line-height: 1.1;
    letter-spacing: -1px;
    white-space: nowrap;
  }
  .artist-name {
    display: block;
    margin: 14px 0 14px 90px;
    font-size: 36px;
    line-height: 1;
    letter-spacing: 0;
    text-transform: uppercase;
    white-space: nowrap;
  }
  .mosaic-art {
    position: absolute;
    left: 0;
    top: 502px;
    width: 1200px;
    height: 698px;
    background: linear-gradient(125deg,
      var(--mosaic-red) 0%,
      var(--mosaic-yellow) 35%,
      var(--mosaic-orange) 65%,
      var(--mosaic-gold) 100%);
  }
</style>
</head>
<body>
  <main class="cover">
    <section class="title-band">
      <div class="backdrop-letters" aria-hidden="true">Pa</div>
      <h1 class="title-block">
        <span class="title-line">Paper</span>
        <span class="artist-name">Marcus Holloway</span>
        <span class="title-line">Lanterns</span>
      </h1>
    </section>
    <div class="mosaic-art" role="img" aria-label="Abstract stained-glass mosaic of overlapping red, yellow, orange, green, blue and purple triangles crossed by thin black lines"></div>
  </main>
</body>
</html>
```